UI design for a mobile app that manages color schemes/pallettes

Should look cool, different, and modern.
The UI colors should not compete with pallette colors (as much as possible)
Features:
Currently looking for 3 pages/screens for the app: Browse through all palettes, view/edit a single palette, import
Features to include in the UI:
- View the list of color palettes (each list item includes a preview showing all colors in that color palette)
- View a particular color palette.
- Each displayed color should show:
- hex value
- rgb(255, 255, 255) value
- Name of pallete
- Button to copy the palette to a new pallette
- Sliders to change the properties (hue, saturation, value) or all colors in the palette at once
- Ability to add color
- Ability to remove color
- Switch background color that the pallete is displayed on: (black, mid gray, white, custom)
- A page that allows you to import palettes from a folder
Look and feel
Each slider illustrates characteristics of the customer's brand and the style your logo design should communicate.

```html
<!DOCTYPE html>
<html lang="en">
<head>
<meta charset="utf-8">
<title>Hueva – Colour Palettes</title>
<link href="https://fonts.googleapis.com/css2?family=Roboto:wght@400;500;700&display=swap" rel="stylesheet">
<style>
:root{
  --stage:#2a2a2a;
  --screen:#ffffff;
  --ink:#222222;
  --muted:#777777;
  --line:#e4e4e4;
  --yellow:#f9e43a;
  --rose:#f65b68;
  --blue:#3a628b;
  --darkblue:#2f2a6b;
  --purple:#7a2479;
  --sand:#f5c77b;
  --dark:#4a2356;
  --green:#9a9a1e;
  --brown:#8b4a3c;
  --teal:#2fbf7a;
  --sky:#5a8fe0;
  --amber:#f0a040;
  --add:#2fb84a;
  --remove:#f4582c;
}
*{box-sizing:border-box;margin:0;padding:0}
html,body{width:776px;height:1200px;overflow:hidden}
body{background:var(--stage);font-family:'Roboto',sans-serif;color:var(--ink);position:relative}
.screen{position:absolute;width:340px;height:540px;background:var(--screen);overflow:hidden;border-radius:4px;box-shadow:0 4px 14px rgba(0,0,0,.4)}
.s-browse-a{left:26px;top:30px}
.s-browse-b{left:410px;top:30px}
.s-import{left:26px;top:620px}
.s-edit{left:410px;top:620px}
.topbar{height:46px;display:flex;align-items:center;padding:0 14px;gap:10px;border-bottom:1px solid var(--line)}
.brand{font-weight:700;font-size:15px;color:var(--ink)}
.topbar .spacer{flex:1}
.title{text-align:center;font-weight:700;font-size:12px;letter-spacing:.6px;padding:14px 0 12px}
.grid{display:grid;grid-template-columns:repeat(3,1fr);gap:12px 10px;padding:0 14px}
.cell .chip{height:86px}
.cell .name{font-size:11px;font-weight:700;margin-top:6px}
.cell .hex{font-size:10px;margin-top:2px}
.cell .rgb{font-size:8px;color:var(--muted);margin-top:3px}
.import-hero{height:170px;background:linear-gradient(135deg,#5a2a4a,#2e3550 40%,#4a4a2a 70%,#3a2a3a);display:flex;flex-direction:column;align-items:center;justify-content:center;gap:14px;color:#fff}
.import-hero .icon{width:52px;height:52px;border-radius:50%;background:rgba(255,255,255,.85);display:flex;align-items:center;justify-content:center}
.import-hero p{font-size:12px;font-weight:500}
.steps{background:#f3f2f0;height:324px}
.step{text-align:center;padding:20px 40px;border-bottom:1px solid #d8d8d8;height:108px}
.step:last-child{border-bottom:none}
.step h3{font-size:14px;font-weight:700;letter-spacing:.5px;margin-bottom:8px}
.step p{font-size:10px;color:#444;line-height:1.4}
.edit{padding:18px 22px}
.big-chip{height:150px;background:var(--rose)}
.chip-meta{display:flex;justify-content:space-between;align-items:flex-end;font-size:10px;margin-top:10px;color:#444}
.group-label{font-size:10px;margin:26px 0 10px}
.slider{display:flex;align-items:center;gap:8px;margin-bottom:10px;font-size:9px}
.slider .track{flex:1;height:5px;border-radius:3px;position:relative}
.slider .thumb{position:absolute;top:-4px;width:13px;height:13px;border-radius:50%;background:#fff;border:1px solid #999}
.slider .val{border:1px solid #bbb;font-size:8px;padding:2px 4px;width:34px}
.t-r{background:linear-gradient(90deg,#005b68,#ff5b68)}
.t-g{background:linear-gradient(90deg,#fd0068,#fdff68)}
.t-b{background:linear-gradient(90deg,#fd5b00,#fd5bff)}
.hex-row{display:flex;align-items:center;gap:14px;margin-top:24px;font-size:10px}
.hex-row .field{flex:1;border:1px solid #bbb;padding:6px 8px;display:flex;justify-content:space-between}
.actions{display:flex;gap:16px;margin-top:24px}
.btn{flex:1;height:30px;color:#fff;font-size:10px;font-weight:700;display:flex;align-items:center;justify-content:center}
.btn-add{background:var(--add)}
.btn-remove{background:var(--remove)}
</style>
</head>
<body>

<section class="screen s-browse-a">
  <header class="topbar">
    <svg width="16" height="12" viewBox="0 0 16 12"><path d="M0 1h16M0 6h16M0 11h16" stroke="#222" stroke-width="2"/></svg>
    <span class="brand">Hueva</span><span class="spacer"></span>
    <svg width="15" height="15" viewBox="0 0 15 15"><circle cx="6" cy="6" r="4.5" fill="none" stroke="#222" stroke-width="2"/><path d="M9.5 9.5L14 14" stroke="#222" stroke-width="2"/></svg>
    <svg width="15" height="15" viewBox="0 0 15 15"><circle cx="7.5" cy="7.5" r="5" fill="none" stroke="#222" stroke-width="3" stroke-dasharray="2.5 1.4"/><circle cx="7.5" cy="7.5" r="2" fill="#222"/></svg>
  </header>
  <h2 class="title">COLOUR PALETTES</h2>
  <div class="grid">
    <div class="cell"><div class="chip" style="background:var(--yellow)"></div><div class="name">Yellow</div><div class="hex">#f9e43a</div><div class="rgb">RGB:249,228,58</div></div>
    <div class="cell"><div class="chip" style="background:var(--rose)"></div><div class="name">Rose</div><div class="hex">#f65b68</div><div class="rgb">RGB:253,91,104</div></div>
    <div class="cell"><div class="chip" style="background:var(--blue)"></div><div class="name">Blue</div><div class="hex">#3A628B</div><div class="rgb">RGB:58,98,139</div></div>
    <div class="cell"><div class="chip" style="background:var(--darkblue)"></div><div class="name">Dark Blue</div><div class="hex">#2f2a6b</div><div class="rgb">RGB:47,42,107</div></div>
    <div class="cell"><div class="chip" style="background:var(--purple)"></div><div class="name">Purple</div><div class="hex">#7a2479</div><div class="rgb">RGB:122,36,121</div></div>
    <div class="cell"><div class="chip" style="background:var(--sand)"></div><div class="name">Sand</div><div class="hex">#f5c77b</div><div class="rgb">RGB:245,199,123</div></div>
    <div class="cell"><div class="chip" style="background:var(--dark)"></div><div class="name">Dark</div><div class="hex">#4a2356</div><div class="rgb">RGB:74,35,86</div></div>
    <div class="cell"><div class="chip" style="background:var(--green)"></div><div class="name">Green</div><div class="hex">#9a9a1e</div><div class="rgb">RGB:154,154,30</div></div>
    <div class="cell"><div class="chip" style="background:var(--brown)"></div><div class="name">Brown</div><div class="hex">#8b4a3c</div><div class="rgb">RGB:139,74,60</div></div>
    <div class="cell"><div class="chip" style="background:var(--teal)"></div></div>
    <div class="cell"><div class="chip" style="background:var(--sky)"></div></div>
    <div class="cell"><div class="chip" style="background:var(--amber)"></div></div>
  </div>
</section>

<section class="screen s-browse-b">
  <header class="topbar">
    <svg width="16" height="12" viewBox="0 0 16 12"><path d="M0 1h16M0 6h16M0 11h16" stroke="#222" stroke-width="2"/></svg>
    <span class="brand">Hueva</span><span class="spacer"></span>
    <svg width="15" height="15" viewBox="0 0 15 15"><circle cx="6" cy="6" r="4.5" fill="none" stroke="#222" stroke-width="2"/><path d="M9.5 9.5L14 14" stroke="#222" stroke-width="2"/></svg>
    <svg width="15" height="15" viewBox="0 0 15 15"><circle cx="7.5" cy="7.5" r="5" fill="none" stroke="#222" stroke-width="3" stroke-dasharray="2.5 1.4"/><circle cx="7.5" cy="7.5" r="2" fill="#222"/></svg>
  </header>
  <h2 class="title">COLOUR PALETTES</h2>
  <div class="grid">
    <div class="cell"><div class="chip" style="background:var(--yellow)"></div><div class="name">Yellow</div><div class="hex">#f9e43a</div><div class="rgb">RGB:249,228,58</div></div>
    <div class="cell"><div class="chip" style="background:var(--rose)"></div><div class="name">Rose</div><div class="hex">#f65b68</div><div class="rgb">RGB:253,91,104</div></div>
    <div class="cell"><div class="chip" style="background:var(--blue)"></div><div class="name">Blue</div><div class="hex">#3A628B</div><div class="rgb">RGB:58,98,139</div></div>
    <div class="cell"><div class="chip" style="background:var(--darkblue)"></div><div class="name">Dark Blue</div><div class="hex">#2f2a6b</div><div class="rgb">RGB:47,42,107</div></div>
    <div class="cell"><div class="chip" style="background:var(--purple)"></div><div class="name">Purple</div><div class="hex">#7a2479</div><div class="rgb">RGB:122,36,121</div></div>
    <div class="cell"><div class="chip" style="background:var(--sand)"></div><div class="name">Sand</div><div class="hex">#f5c77b</div><div class="rgb">RGB:245,199,123</div></div>
    <div class="cell"><div class="chip" style="background:var(--dark)"></div><div class="name">Dark</div><div class="hex">#4a2356</div><div class="rgb">RGB:74,35,86</div></div>
    <div class="cell"><div class="chip" style="background:var(--green)"></div><div class="name">Green</div><div class="hex">#9a9a1e</div><div class="rgb">RGB:154,154,30</div></div>
    <div class="cell"><div class="chip" style="background:var(--brown)"></div><div class="name">Brown</div><div class="hex">#8b4a3c</div><div class="rgb">RGB:139,74,60</div></div>
    <div class="cell"><div class="chip" style="background:var(--teal)"></div></div>
    <div class="cell"><div class="chip" style="background:var(--sky)"></div></div>
    <div class="cell"><div class="chip" style="background:var(--amber)"></div></div>
  </div>
</section>

<section class="screen s-import">
  <header class="topbar">
    <svg width="16" height="12" viewBox="0 0 16 12"><path d="M0 1h16M0 6h16M0 11h16" stroke="#222" stroke-width="2"/></svg>
    <span class="brand">Hueva</span><span class="spacer"></span>
    <svg width="15" height="15" viewBox="0 0 15 15"><circle cx="6" cy="6" r="4.5" fill="none" stroke="#222" stroke-width="2"/><path d="M9.5 9.5L14 14" stroke="#222" stroke-width="2"/></svg>
    <svg width="15" height="15" viewBox="0 0 15 15"><circle cx="7.5" cy="7.5" r="5" fill="none" stroke="#222" stroke-width="3" stroke-dasharray="2.5 1.4"/><circle cx="7.5" cy="7.5" r="2" fill="#222"/></svg>
  </header>
  <div class="import-hero" role="img" aria-label="Blurred grid of palette swatches behind the import action">
    <div class="icon"><svg width="24" height="24" viewBox="0 0 24 24"><path d="M12 3v11M7 9l5 5 5-5M4 16v4h16v-4" fill="none" stroke="#555" stroke-width="2.2"/></svg></div>
    <p>Import palettes from a folder</p>
  </div>
  <div class="steps">
    <div class="step"><h3>STEP 1</h3><p>Lorem Ipsum is simply dummy text of the printing and typesetting industry</p></div>
    <div class="step"><h3>STEP 2</h3><p>Lorem Ipsum is simply dummy text of the printing and typesetting industry</p></div>
    <div class="step"><h3>STEP 3</h3><p>Lorem Ipsum is simply dummy text of the printing and typesetting industry</p></div>
  </div>
</section>

<section class="screen s-edit">
  <header class="topbar">
    <svg width="16" height="12" viewBox="0 0 16 12"><path d="M0 1h16M0 6h16M0 11h16" stroke="#222" stroke-width="2"/></svg>
    <span class="brand">Hueva</span><span class="spacer"></span>
    <svg width="15" height="15" viewBox="0 0 15 15"><circle cx="6" cy="6" r="4.5" fill="none" stroke="#222" stroke-width="2"/><path d="M9.5 9.5L14 14" stroke="#222" stroke-width="2"/></svg>
    <svg width="15" height="15" viewBox="0 0 15 15"><circle cx="7.5" cy="7.5" r="5" fill="none" stroke="#222" stroke-width="3" stroke-dasharray="2.5 1.4"/><circle cx="7.5" cy="7.5" r="2" fill="#222"/></svg>
  </header>
  <div class="edit">
    <div class="big-chip"></div>
    <div class="chip-meta"><div>ROSE<br>RGB:253,91,104</div><div>#f65b68</div></div>
    <div class="group-label">RGB</div>
    <div class="slider"><span>R:</span><div class="track t-r"><span class="thumb" style="left:90%"></span></div><span class="val">253 ▾</span></div>
    <div class="slider"><span>G:</span><div class="track t-g"><span class="thumb" style="left:33%"></span></div><span class="val">91 ▾</span></div>
    <div class="slider"><span>B:</span><div class="track t-b"><span class="thumb" style="left:38%"></span></div><span class="val">104 ▾</span></div>
    <div class="hex-row"><span>HEX</span><div class="field"><span>#f65b68</span><span>▾</span></div></div>
    <div class="actions"><div class="btn btn-add">ADD</div><div class="btn btn-remove">REMOVE</div></div>
  </div>
</section>

</body>
</html>
```